Packaging design (small box) for Zendra 5/6 cable (keychain cable)

we need a packaging to sell our cellphone cable.

1)I want the word "BRIX" on the life side in a stylish way...
2)The product must be mostly visible (not hidden with graphic or design)
3)Please design the sides of the packaging (colors,graphics,etc)
4)Please integrate my logo on the packaging (files 3) you can change the colour of the logo if you want.
Please check the attached files: The packaging will be exactly like this with the same material and size (file 2) (the design on the packaging of this picture is the degin by defaut from our supplier).

-They will be put in a counterdisplay

Size of the packaging:
W:36mm H:130mm D:17mm
We trust your creativity!

Attached files the sketch of our packaging and our products to inspire you.

Target Market(s)

16-35 male and female

Industry/Entity Type

Product

Requirements
Must have
• We need the following words on the packaging:
• 1)"Câble compatible pour Zendra 5/6 " (on the front)
• 2) Recharge rapidement (meaning:charge fast)
• 3) Toujours à portée de la main ( meaning always with you)
• 4)BRIX on the left side
• 5)Our logo "Tervane"
Nice to have
• I am really open about your ideas
Should not have

```html
<!DOCTYPE html>
<html lang="fr">
<head>
<meta charset="utf-8">
<title>BRIX – Tervane cable box dieline</title>
<link rel="stylesheet" href="https://fonts.googleapis.com/css2?family=Roboto+Condensed:ital,wght@0,400;0,700;1,300;1,400&display=swap">
<style>
  :root {
    --page: #f2f2f2;
    --cut: #29abe2;
    --paper: #ffffff;
    --ink: #231f20;
    --navy: #16406e;
    --navy-deep: #0f3561;
  }
  html, body {
    margin: 0;
    padding: 0;
    width: 902px;
    height: 1200px;
    overflow: hidden;
    background: var(--page);
  }
  .dieline { display: block; width: 902px; height: 1200px; }
  .cut { fill: var(--paper); stroke: var(--cut); stroke-width: 1; }
  .crease { fill: none; stroke: var(--cut); stroke-width: 0.8; }
  .outline { fill: none; stroke: var(--cut); stroke-width: 1; }
  .front-copy {
    font-family: "Roboto Condensed", sans-serif;
    font-weight: 400;
    font-size: 36px;
    fill: var(--ink);
  }
  .feature {
    font-family: "Roboto Condensed", sans-serif;
    font-style: italic;
    font-weight: 300;
    font-size: 24px;
    fill: var(--ink);
  }
  .slogan {
    font-family: "Roboto Condensed", sans-serif;
    font-weight: 700;
    font-size: 31px;
    fill: #fff;
  }
  .brand-name {
    font-family: "Roboto Condensed", sans-serif;
    font-weight: 400;
    font-size: 14px;
    letter-spacing: 1.5px;
    fill: var(--ink);
  }
  .side-word {
    font-family: "Roboto Condensed", sans-serif;
    font-weight: 400;
    font-size: 78px;
    fill: var(--ink);
  }
  .side-claim {
    font-family: "Roboto Condensed", sans-serif;
    font-style: italic;
    font-weight: 400;
    font-size: 54px;
    fill: var(--ink);
  }
  .divider { stroke: var(--navy); stroke-width: 3; }
</style>
</head>
<body>
<svg class="dieline" viewBox="0 0 902 1200" xmlns="http://www.w3.org/2000/svg">
  <defs>
    <linearGradient id="side-art" x1="0" y1="0" x2="0.3" y2="1">
      <stop offset="0" stop-color="#1f74b4"/>
      <stop offset="0.35" stop-color="#5f9fd8"/>
      <stop offset="0.7" stop-color="#3a78bb"/>
      <stop offset="1" stop-color="#cfe1f3"/>
    </linearGradient>
    <radialGradient id="slogan-band" cx="0.5" cy="0.5" r="0.7">
      <stop offset="0" stop-color="#2a73b6"/>
      <stop offset="1" stop-color="#0f3561"/>
    </radialGradient>
    <filter id="shadow" x="-10%" y="-10%" width="130%" height="130%">
      <feDropShadow dx="8" dy="8" stdDeviation="6" flood-color="#000" flood-opacity="0.25"/>
    </filter>
  </defs>

  <!-- flaps and panels -->
  <g class="box" filter="url(#shadow)">
    <path class="cut" d="M128,228 V160 Q128,154 134,154 H196 Q202,154 202,160 V228 Z"/>
    <path class="cut" d="M212,228 V110 Q212,100 222,100 H404 Q414,100 414,110 V228 Z"/>
    <path class="cut" d="M424,228 V160 Q424,154 430,154 H492 Q498,154 498,160 V228 Z"/>
    <path class="cut" d="M510,228 V142 Q510,132 520,132 H702 Q712,132 712,142 V228 Z"/>
    <path class="cut" d="M128,958 V1026 Q128,1032 134,1032 H196 Q202,1032 202,1026 V958 Z"/>
    <path class="cut" d="M212,958 V1078 Q212,1088 222,1088 H404 Q414,1088 414,1078 V958 Z"/>
    <path class="cut" d="M424,958 V1026 Q424,1032 430,1032 H492 Q498,1032 498,1026 V958 Z"/>
    <rect class="cut" x="117" y="228" width="595" height="730"/>
    <path class="cut" d="M712,228 L774,238 L774,952 L712,958 Z"/>
  </g>

  <!-- creases -->
  <line class="crease" x1="212" y1="144" x2="414" y2="144"/>
  <line class="crease" x1="212" y1="1044" x2="414" y2="1044"/>
  <line class="crease" x1="256" y1="144" x2="259" y2="152"/>
  <line class="crease" x1="370" y1="144" x2="367" y2="152"/>
  <line class="crease" x1="256" y1="1044" x2="259" y2="1036"/>
  <line class="crease" x1="370" y1="1044" x2="367" y2="1036"/>

  <!-- hanger hole -->
  <path class="outline" d="M574,180 H600 Q602,162 612,162 Q622,162 624,180 H650 Q658,180 658,190 Q658,200 650,200 H574 Q566,200 566,190 Q566,180 574,180 Z"/>

  <!-- left side panel : BRIX -->
  <g class="side-panel side-left">
    <rect x="117" y="228" width="95" height="730" fill="url(#side-art)" role="img" aria-label="Blue sweeping curve artwork on the side panel"/>
    <text class="side-word" transform="translate(143,290) rotate(90)">BRIX</text>
    <g class="side-brand">
      <circle cx="172" cy="884" r="26" fill="var(--navy)"/>
      <text class="brand-name" transform="translate(130,844) rotate(90)">TERVANE</text>
    </g>
  </g>

  <!-- front panel -->
  <g class="face face-front">
    <circle cx="362" cy="272" r="24" fill="var(--navy)"/>
    <text class="brand-name" x="399" y="312" text-anchor="end">TERVANE</text>
    <text class="front-copy">
      <tspan x="234" y="580">Câble</tspan>
      <tspan x="234" y="624">compatible</tspan>
      <tspan x="234" y="668">pour</tspan>
      <tspan x="234" y="712">Zendra 5/6</tspan>
    </text>
    <line class="divider" x1="212" y1="730" x2="414" y2="730"/>
    <g class="charge-icon" transform="translate(254,758)">
      <circle r="16" fill="var(--navy)"/>
      <rect x="-9" y="-6" width="16" height="12" rx="2" fill="none" stroke="#fff" stroke-width="2"/>
      <rect x="7" y="-2" width="3" height="4" fill="#fff"/>
      <path d="M0,-8 L-4,1 H0 L-2,8 L4,-2 H0 Z" fill="#fff"/>
    </g>
    <text class="feature"><tspan x="276" y="767">RECHARGE</tspan><tspan x="258" y="795">RAPIDEMENT</tspan></text>
    <rect x="212" y="810" width="202" height="148" fill="url(#slogan-band)"/>
    <text class="slogan" text-anchor="middle">
      <tspan x="313" y="856">TOUJOURS</tspan>
      <tspan x="313" y="891">À PORTÉE</tspan>
      <tspan x="313" y="926">DE LA MAIN</tspan>
    </text>
  </g>

  <!-- right side panel : RECHARGE RAPIDEMENT -->
  <g class="side-panel side-right">
    <rect x="414" y="228" width="96" height="730" fill="url(#side-art)" role="img" aria-label="Blue sweeping curve artwork on the side panel"/>
    <text class="side-claim" transform="translate(481,836) rotate(-90)" textLength="544" lengthAdjust="spacingAndGlyphs">RECHARGE RAPIDEMENT</text>
    <g class="battery-icon" transform="translate(461,884)">
      <circle r="27" fill="var(--navy)"/>
      <circle r="22" fill="none" stroke="#fff" stroke-width="2"/>
      <rect x="-8" y="-12" width="16" height="24" rx="2" fill="none" stroke="#fff" stroke-width="2.5"/>
      <rect x="-3" y="-15" width="6" height="3" fill="#fff"/>
      <path d="M2,-9 L-5,2 H0 L-2,9 L5,-2 H0 Z" fill="#fff"/>
    </g>
  </g>

  <!-- back panel -->
  <g class="face face-back">
    <circle cx="660" cy="272" r="24" fill="var(--navy)"/>
    <text class="brand-name" x="697" y="312" text-anchor="end">TERVANE</text>
    <text class="front-copy">
      <tspan x="532" y="580">Câble</tspan>
      <tspan x="532" y="624">compatible</tspan>
      <tspan x="532" y="668">pour</tspan>
      <tspan x="532" y="712">Zendra 5/6</tspan>
    </text>
    <line class="divider" x1="510" y1="730" x2="712" y2="730"/>
    <g class="charge-icon" transform="translate(552,758)">
      <circle r="16" fill="var(--navy)"/>
      <rect x="-9" y="-6" width="16" height="12" rx="2" fill="none" stroke="#fff" stroke-width="2"/>
      <rect x="7" y="-2" width="3" height="4" fill="#fff"/>
      <path d="M0,-8 L-4,1 H0 L-2,8 L4,-2 H0 Z" fill="#fff"/>
    </g>
    <text class="feature"><tspan x="574" y="767">RECHARGE</tspan><tspan x="556" y="795">RAPIDEMENT</tspan></text>
    <rect x="510" y="810" width="202" height="148" fill="url(#slogan-band)"/>
    <text class="slogan" text-anchor="middle">
      <tspan x="611" y="856">TOUJOURS</tspan>
      <tspan x="611" y="891">À PORTÉE</tspan>
      <tspan x="611" y="926">DE LA MAIN</tspan>
    </text>
  </g>

  <!-- panel folds -->
  <rect class="outline" x="117" y="228" width="595" height="730"/>
  <line class="crease" x1="212" y1="228" x2="212" y2="958"/>
  <line class="crease" x1="414" y1="228" x2="414" y2="958"/>
  <line class="crease" x1="510" y1="228" x2="510" y2="958"/>
</svg>
</body>
</html>
```